The house buying company website creation

A slick professional landing page it needs to be a very engaging custom designed landing page.

It must have a lead generation tool/box similar to my competitors that will recognise the address when they start to enter the address or postcode.

My main competitors websites to use ideas from to build trust and look correct are: www.brindlecrestholdings.com quillmarshkeys.com

Target Market(s)

People looking to sell their house or property fast. We will buy their property

Industry/Entity Type

Real Estate

Coding

Coded - Design and coding required

Number of Pages Required

1 page

Requirements
Must have
• A lead generation tool that is similar to my competitors to gather their essential details. (please check www.quillmarshkeys.com or www.brindlecrestholdings.com to see what i want.

It also must have all the aspects my competitors has on their landing page. All companies in this industry have this on the landing page. These include: Logos to build trust. Ours can be The Harbinger Logo, the seen on TV logo, The Evening Quorum online logo. Also we need a step by step process map to show the customer how it works.

If the customer is about to leave the page it Must have flash ups that ask the customer to fill in 4 boxes. first name, surname, email, Phone number and address. Check out quillmarshkeys.com to see what i want.

must have a comparison table similar to my competitors. I can include this on the draft.

Must have my frequently asked questions for google SEO ( I will upload these to here to the winner to add this page at the end.

It must be a slick professional design that tells people they are dealing with a company they can trust who has the funds on hand to purchase hundreds of property.
Nice to have
• It must be a slick professional design that tells people they are dealing with a company they can trust who has the funds on hand to purchase hundreds of property.
Should not have
• Anything cheap or tacky looking.

```html
<!DOCTYPE html>
<html lang="en">
<head>
<meta charset="utf-8">
<title>Brookvale Home Buyers</title>
<link href="https://fonts.googleapis.com/css2?family=Poppins:wght@400;500;600;700&display=swap" rel="stylesheet">
<style>
:root{
  --blue:#1d97e3;
  --blue-deep:#2d6fc4;
  --ink:#1c1f26;
  --text:#3d4350;
  --muted:#6c7280;
  --grey:#eef0f4;
  --white:#ffffff;
  --line:#d7dbe2;
}
*{box-sizing:border-box;margin:0;padding:0}
html,body{width:1200px;height:4640px;overflow:hidden;background:var(--white)}
body{font-family:"Poppins",sans-serif;color:var(--text);position:relative}
section,header,footer{position:absolute;left:0;width:1200px;overflow:hidden}
.abs{position:absolute}
.center{left:0;width:1200px;text-align:center}
.fill{position:absolute}

/* header */
.site-header{top:0;height:122px;background:var(--white)}
.top-band{position:absolute;top:0;right:0;width:870px;height:40px;background:var(--blue);clip-path:polygon(0 0,100% 0,100% 100%,8% 100%)}
.top-band .contact{position:absolute;font-size:12px;color:var(--white);display:flex;align-items:center;gap:8px;line-height:1.1}
.brand{position:absolute;display:flex;align-items:center;gap:10px;font-weight:500;color:var(--blue);letter-spacing:-0.5px;white-space:nowrap}
.brand .mark{border-radius:50%;background:var(--blue)}
.nav{position:absolute;top:73px;left:388px;font-size:14px;color:var(--ink)}
.nav a{color:var(--ink);text-decoration:none;position:absolute;white-space:nowrap}
.nav a.active{color:var(--blue);border-bottom:2px solid var(--blue);padding-bottom:2px}
.btn-blue{background:var(--blue);color:var(--white);font-weight:500;display:flex;align-items:center;justify-content:center;border-radius:3px}

/* hero */
.hero{top:122px;height:647px}
.hero .photo{inset:0;background:linear-gradient(100deg,#3a2a22 0%,#6a4a3a 35%,#8c6f5c 60%,#a6988c 100%)}
.hero .shade{inset:0;background:linear-gradient(90deg,rgba(0,0,0,.45) 0%,rgba(0,0,0,.15) 55%,rgba(0,0,0,0) 100%)}
.hero h1{position:absolute;left:131px;top:148px;font-size:60px;line-height:62px;color:var(--white);font-weight:400;letter-spacing:-1.5px}
.hero h1 strong{font-weight:700}
.hero .lead{position:absolute;left:131px;top:298px;font-size:26px;color:var(--white);font-weight:500;letter-spacing:-0.5px}
.search{position:absolute;background:var(--white);display:flex;align-items:center;padding:8px}
.search span{flex:1;font-size:15px;color:var(--ink);padding-left:16px;letter-spacing:-0.3px}
.search .btn-blue{height:100%;font-size:16px;letter-spacing:-0.3px}

/* intro */
.intro{top:769px;height:501px}
.town{left:0;top:355px;width:1200px;height:146px;background:linear-gradient(180deg,rgba(225,229,236,0) 0%,#e7eaf0 100%)}
.house-photo{left:171px;top:69px;width:315px;height:292px;background:linear-gradient(160deg,#8a7a70 0%,#5f524c 60%,#4a403c 100%)}
.intro h2{position:absolute;left:544px;top:92px;font-size:34px;font-weight:600;color:var(--ink);letter-spacing:-1px}
.intro .strong-lead{position:absolute;left:544px;top:150px;width:500px;font-size:17px;line-height:28px;color:var(--ink);letter-spacing:-0.3px}
.intro .body{position:absolute;left:544px;top:215px;width:500px;font-size:13px;line-height:27px;color:var(--muted);letter-spacing:-0.3px}
.btn-outline{position:absolute;border:2px solid var(--ink);display:flex;align-items:center;justify-content:center;font-size:15px;font-weight:600;color:var(--ink);border-radius:3px;letter-spacing:-0.3px}

/* reasons */
.reasons{top:1270px;height:480px;background:var(--grey)}
.section-title{font-size:36px;font-weight:600;letter-spacing:-1px;color:var(--ink)}
.section-sub{font-size:19px;font-weight:500;letter-spacing:-0.4px;color:var(--ink)}
.benefit{position:absolute;top:230px;width:200px;text-align:center}
.benefit svg{display:block;margin:0 auto 18px}
.benefit h3{font-size:17px;font-weight:600;color:var(--blue);letter-spacing:-0.4px;margin-bottom:10px}
.benefit p{font-size:11.5px;line-height:19px;color:var(--text)}

/* cta band */
.cta{top:1750px;height:313px}
.cta .photo{inset:0;background:linear-gradient(180deg,#5b6b84 0%,#404f68 100%)}
.cta .shade{inset:0;background:rgba(40,55,85,.55)}
.cta h2{top:58px;font-size:34px;font-weight:600;color:var(--white);letter-spacing:-1px}
.cta p{top:106px;font-size:19px;color:var(--white);letter-spacing:-0.4px}

/* how it works */
.how{top:2063px;height:715px;background:var(--blue-deep)}
.how .houses{left:0;top:300px;width:1200px;height:415px;background:linear-gradient(180deg,#3f7bc8 0%,#2f65ad 55%,#23518f 100%)}
.how h2{top:72px;font-size:34px;font-weight:600;color:var(--white);letter-spacing:-1px}
.steps-line{position:absolute;left:256px;top:192px;width:721px;height:2px;background:rgba(255,255,255,.85)}
.step{position:absolute;top:170px;width:180px;text-align:center;color:var(--white)}
.step .num{width:46px;height:46px;margin:0 auto 10px;border:2px solid var(--white);border-radius:50%;background:var(--blue-deep);display:flex;align-items:center;justify-content:center;font-size:22px;font-weight:500}
.step .label{font-size:18px;font-weight:600;line-height:24px;letter-spacing:-0.5px}
.how .close{top:390px;font-size:34px;font-weight:600;color:var(--white);letter-spacing:-1px}
.video{left:292px;top:2542px;width:632px;height:364px;background:linear-gradient(135deg,#d9cdbb 0%,#a99680 55%,#7d6d5d 100%);z-index:2}
.video .play{position:absolute;left:280px;top:146px;width:72px;height:72px;border-radius:50%;background:var(--white);display:flex;align-items:center;justify-content:center}

/* reviews */
.reviews{top:2778px;height:564px}
.reviews h2{top:210px;font-size:36px;font-weight:600;color:var(--blue);letter-spacing:-1px}
.reviews .sub{top:256px;font-size:19px;color:var(--muted);font-weight:500;letter-spacing:-0.4px}
.reviews .quote{top:318px;font-size:21px;font-weight:600;color:var(--ink);letter-spacing:-0.6px}
.reviews .quote b{color:var(--blue);font-size:30px;vertical-align:-6px;margin:0 8px}
.reviews .body{top:364px;font-size:16px;line-height:24px;color:var(--text);letter-spacing:-0.3px}
.reviews .author{top:428px;font-size:17px;color:var(--blue);letter-spacing:-0.3px}
.arrow{position:absolute;top:357px;width:42px;height:42px;border:2px solid #8a909b;border-radius:50%;display:flex;align-items:center;justify-content:center}

/* faq */
.faq{top:3342px;height:460px}
.faq .photo{inset:0;background:linear-gradient(90deg,#f4f6f9 0%,#eef1f5 38%,#c9ccd1 58%,#8f8b86 80%,#6d6a66 100%)}
.faq h2{position:absolute;left:133px;top:106px;font-size:36px;font-weight:600;color:var(--blue);letter-spacing:-1px}
.faq .sub{position:absolute;left:133px;top:158px;font-size:19px;font-weight:500;color:var(--ink);letter-spacing:-0.4px}
.faq-item{position:absolute;left:133px;width:345px;display:flex;justify-content:space-between;align-items:center;font-size:16px;font-weight:500;color:var(--ink);letter-spacing:-0.3px}
.faq-item i{font-style:normal;font-size:30px;font-weight:400;color:var(--blue);line-height:1}
.btn-outline-blue{position:absolute;left:133px;top:332px;width:139px;height:45px;border:2px solid var(--blue);color:var(--blue);font-size:15px;font-weight:600;display:flex;align-items:center;justify-content:center;letter-spacing:-0.3px}

/* contact */
.contact-form{top:3802px;height:463px;background:var(--blue)}
.contact-form h2{top:56px;font-size:36px;font-weight:600;color:var(--white);letter-spacing:-1px}
.contact-form .sub{top:111px;font-size:18px;font-weight:600;color:var(--white);letter-spacing:-0.4px}
.field{position:absolute;background:var(--white);font-size:14px;color:var(--ink);padding:13px 0 0 17px;letter-spacing:-0.2px}
.btn-dark{position:absolute;left:512px;top:342px;width:176px;height:45px;background:#4a4f58;color:var(--white);font-size:15px;font-weight:600;border-radius:4px;display:flex;align-items:center;justify-content:center;letter-spacing:-0.3px}

/* footer */
.site-footer{top:4265px;height:375px;background:#f7f8fa}
.footer-col{position:absolute;top:102px;font-size:13px;line-height:32px;color:var(--ink)}
.footer-col.main{font-weight:600}
.footer-col h4{font-size:13px;font-weight:600}
.footer-col a{display:block;color:var(--text);text-decoration:underline;font-size:12px;line-height:27px}
.map{left:798px;top:95px;width:270px;height:110px;background:linear-gradient(135deg,#e7e9ec,#d5dae0);border-bottom:4px solid #f2b94a}
.socials{position:absolute;top:253px;left:522px;display:flex;gap:6px}
.socials span{width:34px;height:34px;border:2px solid var(--blue);border-radius:50%}
.footer-rule{position:absolute;left:28px;top:308px;width:1144px;height:1px;background:var(--line)}
.copyright{top:330px;font-size:13px;color:var(--muted)}
</style>
</head>
<body>

<header class="site-header">
  <div class="top-band">
    <div class="contact" style="left:462px;top:13px">
      <svg width="16" height="12" viewBox="0 0 16 12"><rect x="0.5" y="0.5" width="15" height="11" fill="none" stroke="#fff"/><path d="M1 1l7 6 7-6" fill="none" stroke="#fff"/></svg>
      hello@brookvalehomes.net
    </div>
    <div class="contact" style="left:695px;top:7px">
      <svg width="18" height="18" viewBox="0 0 24 24"><path d="M5 3h4l2 5-3 2a12 12 0 006 6l2-3 5 2v4a2 2 0 01-2 2A18 18 0 013 5a2 2 0 012-2z" fill="none" stroke="#fff" stroke-width="1.6"/></svg>
      <span>Call Us<br><b style="font-weight:600;font-size:13px">555.014.2290</b></span>
    </div>
  </div>
  <div class="brand" style="left:62px;top:62px;font-size:21px"><span class="mark" style="width:30px;height:30px"></span>Brookvale Home Buyers</div>
  <nav class="nav">
    <a class="active" style="left:0">Home</a>
    <a style="left:79px">About</a>
    <a style="left:160px">Home Buyers</a>
    <a style="left:290px">How It Works</a>
    <a style="left:420px">FAQ</a>
    <a style="left:481px">Contact Us</a>
  </nav>
  <div class="btn-blue abs" style="left:973px;top:63px;width:158px;height:42px;font-size:15px">Get a cash offer</div>
</header>

<section class="hero">
  <div class="fill photo" role="img" aria-label="Photo of a smiling father carrying his daughter on his shoulders in front of a brick family home"></div>
  <div class="fill shade"></div>
  <h1><strong>We will buy</strong> any type<br>of property fast</h1>
  <p class="lead">Get your cash offer today.</p>
  <div class="search" style="left:131px;top:382px;width:484px;height:60px">
    <span>Enter Keyword or Postcode</span>
    <div class="btn-blue" style="width:168px">Get A Cssh Offer</div>
  </div>
</section>

<section class="intro">
  <div class="fill town" role="img" aria-label="Faint line drawing of a row of town houses"></div>
  <div class="abs house-photo" role="img" aria-label="Family portrait on the steps of their home, framed in a house-shaped illustration"></div>
  <h2>We will buy your property fast</h2>
  <p class="strong-lead">We'll buy any type of property, regardless of the condition and you won't pay solicitor or estate agent fees.</p>
  <p class="body">Lorem Ipsum is simply dummy text of the printing and typesetting industry. Lorem Ipsum has been the industry's standard dummy text ever since the 1500s, when an unknown printer took a galley of type and scrambled it to make a type specimen book. It has survived not only five centuries,</p>
  <div class="btn-outline" style="left:548px;top:350px;width:136px;height:47px">Learn More</div>
</section>

<section class="reasons">
  <h2 class="abs center section-title" style="top:116px">Reason People Work with Us</h2>
  <p class="abs center section-sub" style="top:168px">Benefits of working with us oer a realtor.</p>

  <div class="benefit" style="left:152px">
    <svg width="70" height="80" viewBox="0 0 70 80" fill="none" stroke="#1d97e3" stroke-width="2"><path d="M35 18a18 18 0 00-11 32v10h22V50a18 18 0 00-11-32z"/><path d="M28 66h14M30 72h10M35 60V40M30 40h10"/><path d="M35 2v8M12 12l6 6M58 12l-6 6M4 36h8M58 36h8"/></svg>
    <h3>Quick Turnaround</h3>
    <p>Lorem Ipsum is simply text of<br>printing and typesetting industry.<br>Lorem Ipsum has Lorem Ipsum</p>
  </div>
  <div class="benefit" style="left:379px">
    <svg width="70" height="80" viewBox="0 0 70 80" fill="none" stroke="#1d97e3" stroke-width="2.2"><circle cx="35" cy="40" r="32"/><path d="M20 40l11 11 20-22"/></svg>
    <h3>Zero Fees</h3>
    <p>Lorem Ipsum is simply text of<br>printing and typesetting industry.<br>Lorem Ipsum has Lorem Ipsum</p>
  </div>
  <div class="benefit" style="left:613px">
    <svg width="86" height="80" viewBox="0 0 86 80" fill="none" stroke="#1d97e3" stroke-width="2"><path d="M4 30l16-14 12 10 12-4 12 4 12-10 16 14-10 12-6-4-20 20a5 5 0 01-8-6l-4 4a5 5 0 01-8-6l-4 4a5 5 0 01-8-6l-6-8z"/><path d="M38 28l-10 10a4 4 0 006 6l10-8 16 14"/></svg>
    <h3>Stress &amp; Hassle Free</h3>
    <p>Lorem Ipsum is simply text of<br>printing and typesetting industry.<br>Lorem Ipsum has Lorem Ipsum</p>
  </div>
  <div class="benefit" style="left:848px">
    <svg width="86" height="80" viewBox="0 0 86 80" fill="none" stroke="#1d97e3" stroke-width="2"><path d="M6 50l36-16 36 16-36 16z"/><path d="M6 42l36-16 36 16-36 16z"/><path d="M6 34l36-16 36 16-36 16z"/><path d="M6 26l36-16 36 16-36 16z"/></svg>
    <h3>Could Hard Cash Fast</h3>
    <p>Lorem Ipsum is simply text of<br>printing and typesetting industry.<br>Lorem Ipsum has Lorem Ipsum</p>
  </div>
</section>
<div class="abs" style="left:574px;top:1246px;width:52px;height:52px;border-radius:50%;background:var(--blue);border:6px solid var(--grey)"></div>

<section class="cta">
  <div class="fill photo" role="img" aria-label="Family sitting on the front porch steps of a house between white balusters"></div>
  <div class="fill shade"></div>
  <h2 class="abs center">Get your cash offer today</h2>
  <p class="abs center">We buy property directly and you won't pay any agent's fees.</p>
  <div class="search" style="left:367px;top:165px;width:463px;height:56px">
    <span>Enter Keyword or Postcode</span>
    <div class="btn-blue" style="width:158px">Get A Cssh Offer</div>
  </div>
</section>

<section class="how">
  <div class="fill houses" role="img" aria-label="Blue tinted photo of a large suburban house with trees"></div>
  <h2 class="abs center">How It Works</h2>
  <div class="steps-line"></div>
  <div class="step" style="left:166px"><div class="num">1</div><div class="label">Call or Email Us</div></div>
  <div class="step" style="left:346px"><div class="num">2</div><div class="label">Speak to out<br>Expert</div></div>
  <div class="step" style="left:526px"><div class="num">3</div><div class="label">Schedule a Quick<br>Walk-Through</div></div>
  <div class="step" style="left:706px"><div class="num">4</div><div class="label">Receive a Cash<br>Offer</div></div>
  <div class="step" style="left:887px"><div class="num">5</div><div class="label">Get Paid</div></div>
  <h3 class="abs center close">Close as Fast as 7 Days!</h3>
</section>

<div class="abs video" role="img" aria-label="Video still of a family relaxing on a sofa in a bright living room">
  <div class="play"><svg width="28" height="32" viewBox="0 0 28 32"><path d="M4 2l22 14L4 30z" fill="#111"/></svg></div>
</div>

<section class="reviews">
  <h2 class="abs center">Reviews</h2>
  <p class="abs center sub">Hear from satisfied customers</p>
  <p class="abs center quote"><b>“</b>Lorem Ipsum is simply dummy text<b>”</b></p>
  <p class="abs center body">the printing and typesetting industry. Lorem Ipsum has been the industry's<br>standard dummy text ever since the 1500s, when an unknown printer took</p>
  <p class="abs center author">By Author Name</p>
  <div class="arrow" style="left:222px"><svg width="14" height="18" viewBox="0 0 14 18"><path d="M11 2L3 9l8 7" fill="none" stroke="#8a909b" stroke-width="2"/></svg></div>
  <div class="arrow" style="left:936px"><svg width="14" height="18" viewBox="0 0 14 18"><path d="M3 2l8 7-8 7" fill="none" stroke="#8a909b" stroke-width="2"/></svg></div>
</section>

<section class="faq">
  <div class="fill photo" role="img" aria-label="Smiling couple looking at a laptop together"></div>
  <h2>Questions?</h2>
  <p class="sub">We have the answers.</p>
  <div class="faq-item" style="top:208px">How fast does this work?<i>+</i></div>
  <div class="faq-item" style="top:246px">What are your fees?<i>+</i></div>
  <div class="faq-item" style="top:285px">What if my home is not in good shape?<i>+</i></div>
  <div class="btn-outline-blue">More FAQs</div>
</section>

<section class="contact-form">
  <h2 class="abs center">Contact Form</h2>
  <p class="abs center sub">Speak with a our Expert today.</p>
  <div class="field" style="left:252px;top:156px;width:227px;height:44px">Full Name</div>
  <div class="field" style="left:486px;top:156px;width:227px;height:44px">Phone</div>
  <div class="field" style="left:720px;top:156px;width:227px;height:44px">Email</div>
  <div class="field" style="left:252px;top:209px;width:695px;height:52px">Street Address</div>
  <div class="field" style="left:252px;top:270px;width:227px;height:43px">City</div>
  <div class="field" style="left:486px;top:270px;width:227px;height:43px">State</div>
  <div class="field" style="left:720px;top:270px;width:227px;height:43px">Zip</div>
  <div class="btn-dark">Get a Cash Offer</div>
</section>

<footer class="site-footer">
  <div class="brand" style="left:128px;top:140px;font-size:16px"><span class="mark" style="width:24px;height:24px"></span>Brookvale Home Buyers</div>
  <div class="footer-col main" style="left:382px">HOME<br>ABOUT<br>HOME BUYERS<br>HOW IT WORKS</div>
  <div class="footer-col" style="left:533px;top:96px"><h4>SERVICES</h4><a>Residential</a><a>Commercial</a><a>FAQs</a></div>
  <div class="footer-col" style="left:665px;top:96px"><h4>CONTACT</h4><a>FAQ</a><a>Testimonials</a><a>Contact Us</a></div>
  <div class="abs map" role="img" aria-label="Map showing the office location with a red pin"></div>
  <div class="socials"><span></span><span></span><span></span><span></span></div>
  <div class="footer-rule"></div>
  <p class="abs center copyright">© 2021 Brookvale Home Buyers. All Rights are Reserved.</p>
</footer>

</body>
</html>
```